Wine label refresh

We are wanting to modify our Corran Hollow label to include a picture on it.
I have attached the pictures below which we would like on the label. They are of the Corran Hollow vineyard. I have also attached an example of another label with a picture on it that we like the style of.
Updates
Industry/Entity Type
Vineyard
Requirements
Must have
- The Corran Hollow text must stay the same but can be moved down. It still needs to be the same size though.
Marlborough Sauvignon Blanc should remain in the same font and roughly the same size.
Wine of New Zealand also must stay but could potentially be moved.
Nice to have
- It would be nice if we could keep the PM logo on the front label but feel free to experiment with where this goes.

```html
<!DOCTYPE html>
<html lang="en">
<head>
<meta charset="utf-8">
<title>Corran Hollow – Marlborough Sauvignon Blanc 2012</title>
<link rel="stylesheet" href="https://fonts.googleapis.com/css2?family=Cormorant+Garamond:wght@500&family=Pinyon+Script&family=Raleway:wght@300&display=swap">
<style>
  :root {
    --paper: #ffffff;
    --ink: #111111;
    --gold: #d99a00;
    --wine-red: #c4173a;
    --taupe: #b9aea4;
    --vine-sky: #cfd2d4;
    --vine-hill: #8fa06a;
    --vine-green: #4f8a32;
  }
  * { margin: 0; padding: 0; box-sizing: border-box; }
  html, body {
    width: 1200px; height: 1000px; overflow: hidden;
    background: var(--paper);
  }
  .label {
    position: relative;
    width: 1200px; height: 1000px;
    background: var(--paper);
  }
  .frame-lines { position: absolute; inset: 0; }
  .monogram {
    position: absolute; left: 0; right: 0; top: 188px;
    text-align: center;
    font-family: "Cormorant Garamond", Georgia, serif;
    font-weight: 500; font-size: 40px; line-height: 48px;
    letter-spacing: 2px;
    color: var(--ink);
  }
  .vineyard-photo {
    position: absolute; left: 288px; top: 258px;
    width: 623px; height: 236px;
    background: linear-gradient(to bottom,
      var(--vine-sky) 0%, var(--vine-sky) 28%,
      var(--vine-hill) 42%, #6d8a4a 58%,
      var(--vine-green) 78%, #5c9a38 100%);
  }
  .estate-name {
    position: absolute; left: 0; right: 0; top: 512px;
    text-align: center;
    font-family: "Cormorant Garamond", Georgia, serif;
    font-weight: 500; font-size: 86px; line-height: 90px;
    font-variant: small-caps;
    letter-spacing: 0.09em;
    color: var(--ink);
  }
  .varietal, .vintage {
    position: absolute; left: 0; right: 0;
    text-align: center;
    font-family: "Pinyon Script", cursive;
    color: var(--wine-red);
  }
  .varietal { top: 612px; font-size: 62px; line-height: 80px; }
  .vintage { top: 688px; font-size: 56px; line-height: 70px; }
  .origin {
    position: absolute; left: 0; right: 0; top: 782px;
    text-align: center;
    font-family: "Raleway", "Gill Sans", sans-serif;
    font-weight: 300; font-size: 37px; line-height: 44px;
    letter-spacing: 1px;
    color: var(--taupe);
  }
</style>
</head>
<body>
<main class="label">
  <svg class="frame-lines" width="1200" height="1000" viewBox="0 0 1200 1000" aria-hidden="true">
    <rect x="46.5" y="100.5" width="1110" height="802" fill="none" stroke="var(--ink)" stroke-width="1.5"/>
    <rect x="86" y="139.5" width="1030" height="724" fill="none" stroke="var(--gold)" stroke-width="33"/>
    <rect x="114" y="167" width="974" height="668" fill="none" stroke="var(--gold)" stroke-width="2.5"/>
  </svg>

  <div class="monogram">PM</div>

  <div class="vineyard-photo" role="img" aria-label="Photograph of the Corran Hollow vineyard: rows of green vines leading to a cottage among palm trees, green hills under a grey sky"></div>

  <h1 class="estate-name">Corran Hollow</h1>
  <p class="varietal">Marlborough Sauvignon Blanc</p>
  <p class="vintage">2012</p>
  <p class="origin">WINE OF NEW ZEALAND</p>
</main>
</body>
</html>
```